Box for a Bold Bathroom - stylish minimalist package for a modern upscale brand

We need an adaptable package design using a color label on a brown box, or just a brown box with 2 or 3 color printing. The best design would be one that is adaptable for either use.

Our first products launching under this brand will be a series of medicine cabinets and mirrors, and our cartons can vary in size from 500x100x600 mm to 1200x300x1000 mm

About us: we produce a variety of bathroom fixtures including medicine cabinets, mirrors, vanities, etc. You've likely seen our products - we do manufacturing for Valdrane, Murtello, Fenwick Hollow, Dunmore & Pike, and others.

A version of our logo is attached for reference; we use it in a variety of color mixes depending on application. Vector available if needed or can be used FPO and our team will replace.

These are our colors, please take note and ignore the 'color' field:

Light Blue: C:66%/M:6%/Y:22%/K:0%; H:189° S:65% B:78%
Light Grey: C:35%/M:26%/Y:24%/K:0%; H:213° S:5% B:70%
Dark Blue: C:90%/M:50%/Y:44%/K:20%; H:189° S:82% B:43%
Dark Grey: C:70%/M:60%/Y:54%/K:38%; H:213° S:11% B:30%

Project Deadline Extended
Reason: Some revisions still outstanding before we can make selection, and some submissions we have agreed to wait for. Please submit all work ASAP so our team can provide feedback to you. Thanks!

Target Market(s)

DIY'ers; home renovators

Industry/Entity Type

Home Improvement

Font styles to use
Sans Serif

Requirements
Must have
• 1. Brand logo w/ logotype
• 2. Brand name without logo (can be on shipping mark side)
• 3. Multi-lingual En/Fr/Es (you do not need to include multi-lingual content but must allow space for our own translations if you do not)
• 4. Shipping/Handling Glyphs on 5 sides (all but bottom)
• i.e. fragile, this way up, team lift or mech lift, clamp or no clamp, max-stack
• 5. Two sides should include a marked 4" x 4" area for affixing labels (e.g. UPC, SSCC, etc.) ideally with a dotted line or corner marks or similar.
• 6. Shipping mark details or space for them (should be on the smallest side, only needed on one but can be on both) [see example file of shipping mark informations]
Nice to have
• Design that can be used either with color label on brown box, or brown box only.
• If designing for color label; please see the sample images included. Lifestyle should be prominent, the inside photo being smaller to help show interior features. These photos are obviously not useful for brown-box design.

```html
<!DOCTYPE html>
<html lang="en">
<head>
<meta charset="utf-8">
<title>Clearhaven — Carton Panels</title>
<link rel="stylesheet" href="https://fonts.googleapis.com/css2?family=Jost:wght@400&display=swap">
<style>
  :root {
    --backdrop: #ebebec;
    --kraft: #c9975f;
    --kraft-shade: #bd8b57;
    --kraft-light: #dcaa72;
    --kraft-side: #c8985f;
    --ink: #2e2722;
    --brand-blue: #3db3c5;
    --fold: rgba(46, 39, 34, 0.18);
  }
  * { margin: 0; padding: 0; box-sizing: border-box; }
  html, body {
    width: 1200px;
    height: 1037px;
    overflow: hidden;
    background: var(--backdrop);
  }
  .canvas {
    position: relative;
    width: 1200px;
    height: 1037px;
    font-family: "Jost", sans-serif;
    font-weight: 400;
    color: var(--ink);
  }
  .panel { position: absolute; }
  .panel--top {
    left: 200px; top: 110px; width: 680px; height: 120px;
    background: var(--kraft-light);
    border-bottom: 1px solid var(--fold);
  }
  .panel--front {
    left: 200px; top: 230px; width: 680px; height: 580px;
    background: linear-gradient(160deg, var(--kraft-shade), var(--kraft));
  }
  .panel--side {
    left: 880px; top: 230px; width: 120px; height: 580px;
    background: var(--kraft-side);
    border-left: 1px solid var(--fold);
  }

  .lockup {
    position: absolute;
    display: flex;
    align-items: center;
    gap: 10px;
    letter-spacing: 2px;
    white-space: nowrap;
  }
  .lockup__dot {
    display: block;
    border-radius: 50%;
    background: var(--brand-blue);
    flex: none;
  }
  .panel--top .lockup {
    left: 50%; top: 50%;
    transform: translate(-50%, -50%);
    font-size: 18px;
  }
  .panel--top .lockup__dot { width: 22px; height: 22px; }
  .panel--side .lockup {
    left: 50%; top: 230px;
    transform: translateX(-50%);
    flex-direction: column;
    gap: 8px;
    font-size: 12px;
    letter-spacing: 1.5px;
  }
  .panel--side .lockup__dot { width: 18px; height: 18px; }

  .brand-dot {
    position: absolute;
    left: 82px; top: 98px;
    width: 44px; height: 44px;
    border-radius: 50%;
    background: var(--brand-blue);
  }
  .guide-line { position: absolute; background: var(--ink); }
  .guide-line--vertical { left: 101px; top: 150px; width: 6px; height: 380px; }
  .guide-line--horizontal { left: 134px; top: 117px; width: 516px; height: 6px; }
  .brand-name {
    position: absolute;
    left: 300px; top: 160px;
    font-size: 34px;
    letter-spacing: 4px;
  }

  .handling-glyphs {
    position: absolute;
    right: 36px; bottom: 36px;
    display: flex;
    gap: 8px;
  }
  .handling-glyphs svg { width: 44px; height: 44px; }
  .glyph-frame { fill: none; stroke: var(--ink); stroke-width: 3; }
  .glyph-mark { fill: none; stroke: var(--ink); stroke-width: 3; stroke-linecap: round; stroke-linejoin: round; }
  .glyph-fill { fill: var(--ink); }
</style>
</head>
<body>
<main class="canvas">
  <section class="panel panel--top" aria-label="Carton top panel">
    <div class="lockup">
      <span class="lockup__dot" aria-hidden="true"></span>
      <span class="lockup__name">CLEARHAVEN</span>
    </div>
  </section>

  <section class="panel panel--front" aria-label="Carton front panel">
    <span class="brand-dot" aria-hidden="true"></span>
    <span class="guide-line guide-line--vertical" aria-hidden="true"></span>
    <span class="guide-line guide-line--horizontal" aria-hidden="true"></span>
    <p class="brand-name">CLEARHAVEN</p>

    <div class="handling-glyphs" aria-label="Handling symbols">
      <svg viewBox="0 0 44 44" role="img" aria-label="Recyclable">
        <rect class="glyph-frame" x="2" y="2" width="40" height="40"/>
        <path class="glyph-mark" d="M14 26 A9 9 0 1 1 30 26"/>
        <path class="glyph-fill" d="M26 24 L33 24 L30 30 Z"/>
      </svg>
      <svg viewBox="0 0 44 44" role="img" aria-label="Handle with care">
        <rect class="glyph-frame" x="2" y="2" width="40" height="40"/>
        <rect class="glyph-mark" x="17" y="12" width="10" height="10"/>
        <path class="glyph-mark" d="M10 20 L14 30 L20 33 M34 20 L30 30 L24 33"/>
      </svg>
      <svg viewBox="0 0 44 44" role="img" aria-label="This way up">
        <rect class="glyph-frame" x="2" y="2" width="40" height="40"/>
        <path class="glyph-mark" d="M16 32 V12 M11 17 L16 11 L21 17 M28 32 V12 M23 17 L28 11 L33 17"/>
        <path class="glyph-mark" d="M10 35 H34"/>
      </svg>
      <svg viewBox="0 0 44 44" role="img" aria-label="Fragile">
        <rect class="glyph-frame" x="2" y="2" width="40" height="40"/>
        <path class="glyph-mark" d="M13 10 H31 L29 20 Q22 26 15 20 Z M22 24 V33 M16 34 H28"/>
      </svg>
      <svg viewBox="0 0 44 44" role="img" aria-label="Keep dry">
        <rect class="glyph-frame" x="2" y="2" width="40" height="40"/>
        <path class="glyph-mark" d="M9 21 Q22 6 35 21 Z M22 21 V32 Q22 35 19 34"/>
      </svg>
    </div>
  </section>

  <section class="panel panel--side" aria-label="Carton side panel">
    <div class="lockup">
      <span class="lockup__dot" aria-hidden="true"></span>
      <span class="lockup__name">CLEARHAVEN</span>
    </div>
  </section>
</main>
</body>
</html>
```